NEED BILLBOARDS FOR VELMORANCIA

we need to redo our billboards for our business. we want to have catchy, great billboards that follow standard billboard design rules. we do breast and body cosmetic surgery in Bakersfield, fresno, and stockton ca. see attached for some tips. i would like something creative, but conservative, but funny. we also won finest around 18 years in a row and can give you the logo

Target Market(s)

females 21-45

Industry/Entity Type

plastic surgery of the breast and body

Font styles to use
Serif

Requirements
Nice to have
• funny, catchy
Should not have
• pictures of women that are overly exposed

```html
<!DOCTYPE html>
<html lang="en">
<head>
<meta charset="utf-8">
<title>Velmorancia Billboard</title>
<link href="https://fonts.googleapis.com/css2?family=Tinos&family=Montserrat:wght@300;400&display=swap" rel="stylesheet">
<style>
  :root {
    --ink-gray: #5e5d5f;
    --rose: #d6899f;
    --sage: #a3d0a0;
    --paper: #ffffff;
    --shirt: #f1f0f2;
    --shirt-shade: #e2e1e4;
    --bra-gray: #cfcdd1;
    --skin-light: #f0ddd2;
    --skin: #e6c7b6;
  }
  * { margin: 0; padding: 0; box-sizing: border-box; }
  html, body { width: 1200px; height: 641px; overflow: hidden; background: var(--paper); }
  .billboard { position: relative; width: 1200px; height: 641px; background: var(--paper); overflow: hidden; }

  .hero-photo {
    position: absolute; left: 600px; top: 0; width: 600px; height: 641px;
    background:
      linear-gradient(90deg, var(--paper) 0%, rgba(255,255,255,0.85) 10%, rgba(255,255,255,0) 28%),
      linear-gradient(180deg, rgba(255,255,255,0) 70%, rgba(241,240,242,0.9) 100%),
      linear-gradient(90deg, var(--shirt) 22%, var(--shirt-shade) 34%, var(--skin-light) 42%, var(--skin) 58%, var(--skin-light) 70%, var(--shirt-shade) 82%, var(--shirt) 100%),
      linear-gradient(180deg, var(--skin-light) 0%, var(--bra-gray) 100%);
    background-blend-mode: normal, normal, multiply, normal;
  }

  .headline {
    position: absolute; left: 48px; top: 52px;
    font-family: 'Tinos', serif; font-weight: 400; font-size: 61px; line-height: 70px;
    color: var(--ink-gray); letter-spacing: -0.5px; text-transform: uppercase;
  }

  .brand { position: absolute; left: 58px; top: 357px; display: flex; align-items: center; gap: 10px; }
  .brand-dot { width: 16px; height: 16px; border-radius: 50%; background: var(--rose); }
  .brand-name {
    font-family: 'Tinos', serif; font-size: 41px; color: var(--sage); letter-spacing: 1px; line-height: 1;
  }
  .brand-tagline {
    position: absolute; left: 68px; top: 408px;
    font-family: 'Montserrat', sans-serif; font-weight: 400; font-size: 13px; color: var(--rose);
    letter-spacing: 0.3px;
  }

  .services {
    position: absolute; left: 425px; top: 272px; list-style: none;
    font-family: 'Montserrat', sans-serif; font-weight: 300; font-size: 38px; line-height: 52px;
    color: var(--sage);
  }
  .services li { display: flex; align-items: center; }
  .services li::before {
    content: ""; width: 8px; height: 8px; border-radius: 50%; background: var(--rose);
    margin-right: 12px; transform: translateY(-8px);
  }

  .cta-rule { position: absolute; left: 46px; top: 493px; width: 541px; height: 2px; background: var(--rose); }
  .cta-button {
    position: absolute; left: 79px; top: 471px; width: 474px; height: 46px;
    border: 2px solid var(--rose); border-radius: 23px; background: var(--paper);
    display: flex; align-items: center; justify-content: center;
    font-family: 'Montserrat', sans-serif; font-weight: 400; font-size: 21px; color: var(--rose);
    letter-spacing: 0.3px;
  }

  .phone { position: absolute; left: 85px; top: 538px; display: flex; align-items: center; gap: 16px; }
  .phone-icon { width: 50px; height: 50px; }
  .phone-number { font-family: 'Tinos', serif; font-size: 60px; color: var(--rose); line-height: 1; }
</style>
</head>
<body>
  <main class="billboard">
    <div class="hero-photo" role="img" aria-label="Photo of a woman in a loose white shirt and grey bra with arms crossed, shown from shoulders to waist"></div>

    <h1 class="headline">Bringing your<br>beautiful results</h1>

    <div class="brand">
      <span class="brand-dot"></span>
      <span class="brand-name">VELMORANCIA</span>
    </div>
    <p class="brand-tagline">COSMETIC SURGERY AND MEDSPA</p>

    <ul class="services">
      <li>BREAST</li>
      <li>BODY</li>
      <li>FACE</li>
    </ul>

    <div class="cta-rule"></div>
    <div class="cta-button">BOOK YOUR APPOINTMENT TODAY</div>

    <div class="phone">
      <svg class="phone-icon" viewBox="0 0 50 50" aria-hidden="true">
        <circle cx="25" cy="25" r="23" fill="none" stroke="var(--rose)" stroke-width="2"/>
        <path d="M17 14 l5 -1 l3 7 l-3 3 q2 5 7 7 l3 -3 l7 3 l-1 5 q-3 2 -7 1 q-10 -4 -14 -14 q-1 -5 0 -8 z"
              fill="none" stroke="var(--rose)" stroke-width="2" stroke-linejoin="round"/>
        <path d="M28 14 q6 1 8 8 M28 19 q3 1 4 4" fill="none" stroke="var(--rose)" stroke-width="2" stroke-linecap="round"/>
      </svg>
      <span class="phone-number">(555) 014-2288</span>
    </div>
  </main>
</body>
</html>
```